Pain cream backed by Pro-Athletes "Glacier Ember"

Looking to revamp the label brand.
It's an all-natural pain gel. It heats then cools. Looking for a very sharp look that gets the point of the product use across.
Eveyrthing about the original label can be changed except for the text. It still needs to have the same information but can be any color, font whatever.,
I'll need pdf's and ai files of the design.
Label Size die line is attached.
Original Label is attached.

```html
<!DOCTYPE html>
<html lang="en">
<head>
<meta charset="UTF-8">
<title>Glacier Ember – All-Natural Pain Gel Label</title>
<link href="https://fonts.googleapis.com/css2?family=Bebas+Neue&family=Oswald:wght@500&family=Open+Sans:wght@400&display=swap" rel="stylesheet">
<style>
  :root {
    --page-bg: #ffffff;
    --ember-red: #d42a30;
    --deep-red: #b11c26;
    --plum: #7a3a78;
    --violet: #4a3478;
    --glacier-navy: #221f58;
    --label-ink: #f2f0f0;
    --art-tone-warm: rgba(255, 255, 255, 0.14);
    --art-tone-cool: rgba(255, 255, 255, 0.12);
  }
  * { margin: 0; padding: 0; box-sizing: border-box; }
  html, body {
    width: 1200px;
    height: 1200px;
    overflow: hidden;
    background: var(--page-bg);
  }
  .canvas {
    position: relative;
    width: 1200px;
    height: 1200px;
  }
  .label {
    position: absolute;
    left: 237px;
    top: 50px;
    width: 726px;
    height: 1100px;
    background: linear-gradient(180deg,
      var(--ember-red) 0%,
      var(--deep-red) 28%,
      #8a2d5a 46%,
      var(--plum) 56%,
      var(--violet) 75%,
      var(--glacier-navy) 100%);
    color: var(--label-ink);
  }
  .flame-art {
    position: absolute;
    left: 130px;
    top: 125px;
    width: 487px;
    height: 244px;
    border-radius: 48% 48% 6px 6px;
    background: radial-gradient(ellipse at 50% 80%, var(--art-tone-warm), transparent 72%);
  }
  .brand-name {
    position: absolute;
    left: 0;
    right: 0;
    top: 382px;
    text-align: center;
    font-family: "Bebas Neue", sans-serif;
    font-weight: 400;
    font-size: 128px;
    line-height: 1;
    letter-spacing: 1px;
  }
  .tagline {
    position: absolute;
    left: 0;
    right: 0;
    top: 546px;
    text-align: center;
    font-family: "Oswald", sans-serif;
    font-weight: 500;
    font-size: 46px;
    line-height: 1;
    letter-spacing: 4px;
  }
  .snowflake-art {
    position: absolute;
    left: 142px;
    top: 625px;
    width: 432px;
    height: 187px;
    border-radius: 6px 6px 48% 48%;
    background: radial-gradient(ellipse at 50% 20%, var(--art-tone-cool), transparent 72%);
  }
  .product-type {
    position: absolute;
    left: 0;
    right: 0;
    top: 876px;
    text-align: center;
    font-family: "Oswald", sans-serif;
    font-weight: 500;
    font-size: 44px;
    line-height: 1;
  }
  .volume {
    position: absolute;
    left: 0;
    right: 0;
    top: 934px;
    text-align: center;
    font-family: "Open Sans", sans-serif;
    font-size: 29px;
    line-height: 1;
  }
</style>
</head>
<body>
  <main class="canvas">
    <section class="label">
      <div class="flame-art" role="img" aria-label="Flame illustration in white rising above the product name"></div>
      <h1 class="brand-name">Glacier Ember</h1>
      <p class="tagline">BACK ON YOUR FEET</p>
      <div class="snowflake-art" role="img" aria-label="Half snowflake illustration in white below the tagline"></div>
      <p class="product-type">ALL-NATURAL PAIN GEL</p>
      <p class="volume">100ml (3.2oz)</p>
    </section>
  </main>
</body>
</html>
```